'The Lindqvist Draft' needs a movie poster

We need a movie poster for our short film coming up.

Genre: Drama/Mystery

Plot/Synopsis:
The Lindqvist Draft explores the fraught relationship between creation and destiny, the creator and the created: inspiration, obsession, destruction.
In the opening scene we are introduced to Walter Lindqvist and a young writer, Nora, whose stories play out decades apart and yet are intricately linked. Walter struggles with a block during the writing of his first novel; Nora, obsessed with uncovering her own past is inexplicably drawn to Lindqvist’s house and accepts a room for let from Greta, a strange woman who also resides there. As the two woman avoid delving too deep into each other’s pasts, suspicious of their intentions, Nora discovers that Walter mysteriously died without finishing his debut novel and Greta is most certainly holding something back.
Tensions are raised as Nora settles into Walter’s office and investigates the chattels left behind on his bureau. Accidentally marking a waiting page of manuscript, she unlocks a sixth sense of déjà vu, obsession seeps into possession and the voice of the author comes to life in an unexpected manner in order to enact his long awaited epilogue. With-in the novel, Nora finds the key to her past and confronts Greta with what she uncovers.
Dealing with the dark and destructive side of creativity, The Lindqvist Draft is an edgy mystery with a lurking subtext; Or is it just the greatest plot twist penned by a non-living author.

I have attached for you some images taken from the video camera.
Feel free to add any graphic if you want. I don't have a particular idea of how I want the poster so far so you are pretty free as long as The poster is appealing to the public and make them want to see the film and is related to the synopsis.

-An MoVantReel Production see our logo attached in the pictures
-Director by Tomaso Ruffini
-screenplay by Danny Wolcott

-Staring: (by order of importance)
Marthe Quillon
Lorna Brisbee
Glen Mabbott
Rolf Dunning

-Log line: Are you here to fill those pages?

Feel free to use any of those pictures or any of your design if you have ideas. Or even combine some of our pics with some design of yours.
Nora the lead actress is the young girl on the picture. she has to be in the poster. The other older woman is Greta! She is the supporting role-an important key of the story but very mysterious. (she doesn’t have to be in the poster)

Also it is IMPORTANT for me to have this poster in a format that I can edit as I will need to add some more names in the crew & music credit. Important that you could make the changes for me too include in this price.

Target Market(s)

Film festivals

Industry/Entity Type

Movie

Colors

Designer to choose colors to be used in the design.

Requirements
Must have
• The lead Nora (the young girl) in the poster.
• The producer logo must appear.
• A good title writing style.
• Drama feel.
Nice to have
• It would be nice to incorporate a gun in the design of the title 'The Lindqvist Draft'

```html
<!DOCTYPE html>
<html lang="en">
<head>
<meta charset="utf-8">
<title>The Lindqvist Draft — Poster</title>
<link rel="stylesheet" href="https://fonts.googleapis.com/css2?family=Barlow+Condensed:wght@600&family=Permanent+Marker&family=Courier+Prime:wght@700&display=swap">
<style>
  :root {
    --magenta: #fb12dc;
    --electric-blue: #1e7bff;
    --sky-blue: #2fb2ff;
    --hot-red: #ff2d55;
    --amber: #ffb01f;
    --white: #ffffff;
  }
  html, body { margin: 0; padding: 0; overflow: hidden; background: var(--magenta); }
  .poster {
    position: relative; width: 800px; height: 1200px; overflow: hidden;
    background: var(--magenta); color: var(--white);
  }
  .portrait { position: absolute; left: 0; top: 0; width: 800px; height: 1200px; }
  .cast {
    position: absolute; right: 40px; top: 34px; margin: 0; padding: 0; list-style: none;
    text-align: right; font-family: "Barlow Condensed", sans-serif; font-weight: 600;
    font-size: 36px; line-height: 52px; letter-spacing: 0.5px; text-transform: uppercase;
  }
  .title {
    position: absolute; left: 24px; top: 160px; margin: 0;
    font-family: "Permanent Marker", cursive; font-weight: 400; text-transform: uppercase;
    line-height: 0.82; transform: rotate(-3deg); transform-origin: left top;
  }
  .title span { display: block; }
  .title .the { font-size: 170px; }
  .title .name { font-size: 128px; letter-spacing: -4px; }
  .title .draft { font-size: 170px; }
  .logline {
    position: absolute; left: 0; width: 800px; top: 820px; margin: 0; text-align: center;
    font-family: "Courier Prime", monospace; font-weight: 700; font-size: 21px; line-height: 32px;
  }
  .studio {
    position: absolute; left: 40px; bottom: 44px; display: flex; align-items: center; gap: 8px;
    font-family: "Barlow Condensed", sans-serif; font-weight: 600; font-size: 22px;
  }
  .studio-mark { width: 14px; height: 14px; background: var(--white); }
  .credits {
    position: absolute; right: 40px; bottom: 36px; margin: 0; text-align: right;
    font-family: "Barlow Condensed", sans-serif; font-weight: 600; text-transform: uppercase;
  }
  .credits p { margin: 0; font-size: 36px; line-height: 52px; }
  .credits .role { font-size: 21px; }
</style>
</head>
<body>
<main class="poster">
  <svg class="portrait" viewBox="0 0 800 1200" role="img" aria-label="Heat-map styled portrait of Nora, the lead actress, looking straight at the viewer">
    <defs>
      <radialGradient id="heat" cx="0.52" cy="0.4" r="0.6">
        <stop offset="0" stop-color="#ff2d55"/>
        <stop offset="0.35" stop-color="#f1206f"/>
        <stop offset="0.6" stop-color="#3a5cff"/>
        <stop offset="1" stop-color="#2fb2ff"/>
      </radialGradient>
    </defs>
    <path d="M240 200 C270 150 440 130 500 170 C560 200 580 260 580 330 C585 450 600 600 640 720 C700 760 760 820 780 900 L800 1200 L0 1200 L0 900 C40 820 120 780 170 760 C200 640 205 420 215 300 C220 250 225 220 240 200 Z" fill="url(#heat)"/>
  </svg>

  <ul class="cast">
    <li>Marthe Quillon</li>
    <li>Lorna Brisbee</li>
    <li>Glen Mabbott</li>
    <li>Rolf Dunning</li>
  </ul>

  <h1 class="title">
    <span class="the">The</span>
    <span class="name">Lindqvist</span>
    <span class="draft">Draft</span>
  </h1>

  <p class="logline">Are you here<br>to fill those pages?</p>

  <div class="studio"><span class="studio-mark"></span><span>MoVantReel</span></div>

  <div class="credits">
    <p><span class="role">Directed by</span> Tomaso Ruffini</p>
    <p><span class="role">Screenplay by</span> Danny Wolcott</p>
  </div>
</main>
</body>
</html>
```